General Contractors need a new Crisp updated Card Design

We need a new business card design for our company of 25 years based in Toronto call Holvaster Building Inc. : Our goal is to be the leading commercial contractors in Toronto by providing exceptional value to our clients. We work very hard to deliver professional, quality, service in conjunction with consistent price competitiveness to all of our clients on every single project.

Target Market(s)

Design & Build Clients

Industry/Entity Type

Construction Company

Contact Information for Business Card

Address:
18 North Tamlin Glen Road, Unit 57, Marbrook Vale, ON, K7T 2R9
Office: 905-218-5937

Holvasters Logo
Employee Job Description
Employee Cell Phone #
Employee Email
www.holvaster-example.com

Colors

Designer to choose colors to be used in the design.

Requirements
Must have
• Quote Company Saying:
• "Professional. Quality. Service."
Nice to have
• New Crisp up to date look. simple & fresh ( Not to Busy)
Should not have
• NO BLUE PRINTS ON THE BUSINESS CARDS

```html
<!DOCTYPE html>
<html lang="en">
<head>
<meta charset="utf-8">
<title>Holvaster Building Inc. – Business Card</title>
<link rel="stylesheet" href="https://fonts.googleapis.com/css2?family=Lora:ital,wght@0,400;0,700;1,400&family=Open+Sans:wght@400;600&display=swap">
<style>
  :root {
    --stage: #2a2c2f;
    --card: #231f20;
    --teal: #0d7a6d;
    --sage: #93b5a9;
    --ink-light: #f1f1ef;
    --ink-dark: #2b2a2a;
    --rule: #8a8a8a;
  }
  * { box-sizing: border-box; margin: 0; padding: 0; }
  html, body { width: 1200px; height: 900px; overflow: hidden; }
  body {
    background: var(--stage);
    display: flex;
    align-items: center;
    justify-content: center;
    gap: 40px;
    font-family: "Lora", Georgia, serif;
  }
  .card {
    position: relative;
    width: 540px;
    height: 310px;
    background: var(--card);
    border-radius: 22px;
    overflow: hidden;
    box-shadow: 0 14px 30px rgba(0,0,0,.45);
  }

  /* Front */
  .brand {
    position: absolute;
    top: 88px;
    left: 0; right: 0;
    display: flex;
    align-items: center;
    justify-content: center;
    gap: 18px;
  }
  .brand-square {
    width: 62px; height: 62px;
    background: var(--teal);
  }
  .brand-name {
    color: var(--teal);
    font-weight: 700;
    font-size: 30px;
    line-height: 1.1;
    letter-spacing: 1px;
    text-transform: uppercase;
  }
  .address-band {
    position: absolute;
    left: 0; right: 0; bottom: 0;
    height: 50px;
    background: var(--sage);
    display: flex;
    align-items: center;
    justify-content: center;
    color: var(--ink-dark);
    font-style: italic;
    font-size: 14.5px;
  }

  /* Back */
  .back-mark {
    position: absolute;
    top: 22px; left: 50%;
    width: 34px; height: 34px;
    margin-left: -17px;
    background: var(--teal);
  }
  .motto {
    position: absolute;
    top: 64px; left: 0; right: 0;
    text-align: center;
    color: var(--ink-light);
    font-style: italic;
    font-size: 15px;
  }
  .name-band {
    position: absolute;
    top: 96px; left: 0; right: 0;
    height: 62px;
    background: var(--sage);
    text-align: center;
    padding-top: 8px;
  }
  .person-name {
    color: var(--teal);
    font-weight: 700;
    font-size: 22px;
    letter-spacing: 1px;
  }
  .person-role {
    color: var(--ink-dark);
    font-size: 11px;
    letter-spacing: 1.5px;
  }
  .contacts {
    position: absolute;
    top: 186px; left: 0; right: 0;
    display: flex;
    justify-content: center;
    align-items: stretch;
    font-family: "Open Sans", Arial, sans-serif;
    color: var(--ink-light);
    font-size: 13px;
  }
  .contact-col {
    display: flex;
    flex-direction: column;
    gap: 12px;
    padding: 6px 22px;
  }
  .contact-col.office { align-items: flex-end; }
  .contact-divider { width: 1px; background: var(--rule); }
  .contact-line { display: flex; align-items: center; gap: 9px; }
  .contact-col.office .contact-line { flex-direction: row-reverse; }
  .icon { width: 14px; height: 14px; flex: none; }
</style>
</head>
<body>

  <section class="card card-front" aria-label="Business card front">
    <div class="brand">
      <div class="brand-square"></div>
      <div class="brand-name">Holvaster<br>Building Inc.</div>
    </div>
    <div class="address-band">18 North Tamlin Glen Road, Unit 57, Marbrook Vale, ON, K7T 2R9</div>
  </section>

  <section class="card card-back" aria-label="Business card back">
    <div class="back-mark"></div>
    <p class="motto">"Professional. Quality. Service."</p>
    <div class="name-band">
      <div class="person-name">MARLON VEY</div>
      <div class="person-role">OWNER</div>
    </div>
    <div class="contacts">
      <div class="contact-col office">
        <div class="contact-line">
          <svg class="icon" viewBox="0 0 14 14" aria-hidden="true"><rect x="3.5" y="1" width="7" height="12" rx="1.2" fill="none" stroke="#0d7a6d" stroke-width="1.4"/><circle cx="7" cy="11" r=".8" fill="#0d7a6d"/></svg>
          <span>905-218-5937</span>
        </div>
        <div class="contact-line">
          <svg class="icon" viewBox="0 0 14 14" aria-hidden="true"><rect x="1" y="3" width="12" height="8" fill="#0d7a6d"/><path d="M1 3 L7 8 L13 3" fill="none" stroke="#231f20" stroke-width="1"/></svg>
          <span>email@holvaster-example.com</span>
        </div>
      </div>
      <div class="contact-divider"></div>
      <div class="contact-col cell">
        <div class="contact-line">
          <svg class="icon" viewBox="0 0 14 14" aria-hidden="true"><path d="M3 1.5 L5.5 1.5 L6.5 4.5 L5 5.8 C5.8 7.5 6.6 8.3 8.2 9 L9.5 7.5 L12.5 8.5 L12.5 11 C12.5 12 11.8 12.5 11 12.5 C5.5 12.2 1.8 8.5 1.5 3 C1.5 2.2 2 1.5 3 1.5 Z" fill="#0d7a6d"/></svg>
          <span>123 - xxx- xxxx</span>
        </div>
        <div class="contact-line">
          <svg class="icon" viewBox="0 0 14 14" aria-hidden="true"><circle cx="7" cy="7" r="6" fill="#0d7a6d"/><ellipse cx="7" cy="7" rx="2.6" ry="6" fill="none" stroke="#231f20" stroke-width=".9"/><path d="M1 7 H13 M2 4 H12 M2 10 H12" stroke="#231f20" stroke-width=".9"/></svg>
          <span>www.holvaster-example.com</span>
        </div>
      </div>
    </div>
  </section>

</body>
</html>
```